" Não vendemos nossos serviços "no varejo". Somos chamados a participar de projetos de investimento no Brasil ainda na fase de concepção, sob acordo de confidencialidade, buscando alimentar a modelagem financeira com os inputs tributários que frequentemente são cruciais na definição de viabilidade do projeto. Também somos chamados por nossos clientes para avaliar ou alocar contratualmente riscos decorrentes de contingências fiscais, especialmente em fusões e aquisições de empresas. E, ainda, patrocinar defesas ou pleitos em processos administrativos ou judiciais, sempre tendo como parte adversária o fisco (federal, estadual ou municipal). Atuamos em um ambiente profissional onde ética, compliance, qualidade e comprometimento são premissas. O propósito de nossa empresa é a criação de valor de modo sustentável, em questões fiscais, para negócios empreendidos no Brasil. "

```html
<!DOCTYPE html>
<html lang="pt-BR">
<head>
<meta charset="utf-8">
<title>Lima Prado Torres Advogados – Cartão de visita</title>
<link rel="stylesheet" href="https://fonts.googleapis.com/css2?family=Roboto+Condensed:wght@300;400&display=swap">
<style>
  :root {
    --backdrop: #e4e6ea;
    --card: #ffffff;
    --navy: #2b3a6e;
    --blue: #4a63a8;
    --sky: #8fa6d0;
    --ink-soft: #7f93bd;
    --shadow: rgba(20, 30, 50, 0.18);
  }
  * { margin: 0; padding: 0; box-sizing: border-box; }
  html, body {
    width: 1200px; height: 1200px; overflow: hidden;
    background: var(--backdrop);
    font-family: "Roboto Condensed", "Arial Narrow", sans-serif;
    font-weight: 300;
  }
  .canvas {
    position: relative; width: 1200px; height: 1200px;
    display: flex; flex-direction: column; align-items: center; justify-content: center; gap: 60px;
  }
  .card {
    position: relative; width: 900px; height: 500px;
    background: var(--card);
    box-shadow: 0 10px 30px var(--shadow);
  }
  /* Front */
  .card--front {
    display: flex; align-items: center; justify-content: center; gap: 22px;
  }
  .brand-mark {
    width: 34px; height: 34px; background: var(--navy);
  }
  .brand-name {
    font-size: 40px; letter-spacing: 3px; text-transform: uppercase; color: var(--navy);
    font-weight: 300;
  }
  /* Back */
  .firm-name {
    position: absolute; left: 60px; top: 50px;
    font-size: 30px; line-height: 1.12; letter-spacing: 2px; text-transform: uppercase;
    color: var(--sky);
  }
  .firm-square {
    position: absolute; left: 62px; top: 228px; width: 46px; height: 46px;
    background: var(--blue);
  }
  .contact {
    position: absolute; left: 520px; top: 255px; color: var(--ink-soft);
  }
  .contact__name { font-size: 34px; color: var(--blue); margin-bottom: 10px; }
  .contact__line { font-size: 17px; line-height: 1.45; }
  .address {
    position: absolute; left: 60px; bottom: 50px; color: var(--ink-soft);
    font-size: 17px; line-height: 1.45;
  }
  .address__site { margin-top: 12px; }
</style>
</head>
<body>
  <main class="canvas">
    <section class="card card--front" aria-label="Frente do cartão">
      <span class="brand-mark" aria-hidden="true"></span>
      <span class="brand-name">Lima Prado Torres</span>
    </section>

    <section class="card card--back" aria-label="Verso do cartão">
      <h1 class="firm-name">Lima<br>Prado<br>Torres<br>Advogados</h1>
      <span class="firm-square" aria-hidden="true"></span>

      <div class="contact">
        <p class="contact__name">Helena Torres</p>
        <p class="contact__line">helena@lptadv.com.br</p>
        <p class="contact__line">+55 21 90000 0000</p>
      </div>

      <address class="address" style="font-style: normal;">
        <p>Rua das Acácias 120, 8º andar</p>
        <p>22000-000, Rio de Janeiro, RJ</p>
        <p class="address__site">lptadv.com.br</p>
      </address>
    </section>
  </main>
</body>
</html>
```